Business Card for Coral Reef Shore Dive Lodge
Kelumpang Beach Resort & Dive Tour Sdn. Bhd.
Bright & Fun-filled
Harudin Bin Sulaiman Taib
QRT Marketing & HR Manager
C27-4, Meranti Square, Jalan Tuaran
88450 Kota Kinabalu, SABAH Malaysia.
kelumpangresort@mailnest.example
572918-K (KPL/LN 4721)
logo vector

```html
<!DOCTYPE html>
<html lang="en">
<head>
<meta charset="utf-8">
<title>Kelumpang Stationery Concepts</title>
<link href="https://fonts.googleapis.com/css2?family=Cormorant+Garamond:wght@500;600&family=Montserrat:wght@400;500&display=swap" rel="stylesheet">
<style>
:root{
  --board:#3b2b22;
  --paper:#ffffff;
  --paper-shade:#f1efec;
  --ink:#111111;
  --bronze:#a8805e;
  --bronze-soft:#d9c6b4;
  --grey-flap:#c9c9cb;
  --muted:#8c8a88;
  --card-text:#b9aea3;
  --label:#d8cfc6;
}
*{margin:0;padding:0;box-sizing:border-box}
html,body{width:1200px;height:466px;overflow:hidden;background:var(--board)}
.board{position:relative;width:1200px;height:466px;font-family:"Montserrat",sans-serif}
.board-title{position:absolute;left:12px;top:152px;font-size:9px;font-weight:500;letter-spacing:1.5px;text-transform:uppercase;color:var(--label)}
.label{position:absolute;font-size:6px;letter-spacing:1px;text-transform:uppercase;color:var(--label);white-space:nowrap}
.wordmark{font-family:"Cormorant Garamond",serif;font-weight:600;color:var(--bronze);letter-spacing:2px;text-transform:uppercase;display:flex;align-items:center;gap:5px;white-space:nowrap}
.wordmark .dot{width:6px;height:6px;border-radius:50%;background:var(--bronze)}
.card{position:absolute;left:12px;width:132px;height:54px;background:var(--ink);box-shadow:0 2px 5px rgba(0,0,0,.5)}
.card-front{display:flex;align-items:center;justify-content:center}
.card-front .wordmark{font-size:11px}
.card-back{padding:7px 8px}
.card-back .wordmark{font-size:7px;letter-spacing:1.2px;gap:3px}
.card-back .wordmark .dot{width:4px;height:4px}
.card-name{margin-top:5px;font-size:4.6px;font-weight:500;color:var(--bronze)}
.card-role{font-size:3.8px;color:var(--card-text);margin-bottom:3px}
.card-details{font-size:3.6px;line-height:5px;color:var(--card-text)}
.sheet{position:absolute;top:24px;width:288px;height:420px;background:var(--paper);box-shadow:0 3px 8px rgba(0,0,0,.45)}
.sheet .wordmark{position:absolute;top:34px;font-size:15px}
.sheet .rule{position:absolute;top:30px;height:1px;background:var(--bronze-soft)}
.contact{position:absolute;left:178px;top:22px;font-size:4.5px;line-height:7px;color:var(--muted)}
.mermaid{position:absolute;border-radius:40% 50% 45% 55%;background:radial-gradient(ellipse at 50% 45%,rgba(217,198,180,.55),rgba(217,198,180,0) 70%)}
.footer{position:absolute;left:10px;right:10px;bottom:12px;font-size:4.2px;color:var(--muted);text-align:center;white-space:nowrap}
.envelope{position:absolute;left:792px;width:384px;background:var(--paper);box-shadow:0 3px 7px rgba(0,0,0,.45);overflow:hidden}
.envelope svg{display:block}
.env-front{top:372px;height:66px}
.env-front .wordmark{position:absolute;left:14px;top:10px;font-size:12px}
.env-front .line{position:absolute;left:14px;top:30px;font-size:4.5px;color:var(--muted)}
</style>
</head>
<body>
<main class="board">
  <h1 class="board-title">Stationery Concepts</h1>

  <div class="card card-front" style="top:296px"><span class="wordmark"><span class="dot"></span>Kelumpang</span></div>
  <span class="label" style="left:12px;top:355px">Business Card Front</span>

  <div class="card card-back" style="top:372px">
    <div class="wordmark"><span class="dot"></span>Kelumpang</div>
    <p class="card-name">Harudin Bin Sulaiman Taib</p>
    <p class="card-role">QRT Marketing &amp; HR Manager</p>
    <p class="card-details">C27-4, Meranti Square, Jalan Tuaran, 88450 Kota Kinabalu<br>kelumpangresort@mailnest.example</p>
  </div>
  <span class="label" style="left:12px;top:431px">Business Card Back</span>

  <section class="sheet" style="left:168px">
    <div class="rule" style="left:20px;width:90px"></div>
    <div class="wordmark" style="left:20px"><span class="dot"></span>Kelumpang</div>
    <p class="contact">C27-4, Meranti Square, Jalan Tuaran<br>88450 Kota Kinabalu, Sabah<br>kelumpangresort@mailnest.example<br>572918-K (KPL/LN 4721)</p>
    <div class="mermaid" role="img" aria-label="Faint mermaid illustration" style="left:120px;top:270px;width:150px;height:140px"></div>
  </section>
  <span class="label" style="left:270px;top:449px">Letter Head Option 1</span>

  <section class="sheet" style="left:475px">
    <div class="rule" style="left:94px;width:100px"></div>
    <div class="wordmark" style="left:86px"><span class="dot"></span>Kelumpang</div>
    <div class="mermaid" role="img" aria-label="Faint mermaid illustration" style="left:70px;top:150px;width:120px;height:110px"></div>
    <p class="footer">C27-4, Meranti Square, Jalan Tuaran &nbsp;|&nbsp; 88450 Kota Kinabalu &nbsp;|&nbsp; kelumpangresort@mailnest.example</p>
  </section>
  <span class="label" style="left:578px;top:449px">Letter Head Option 2</span>

  <div class="envelope" style="top:29px;height:103px">
    <svg width="384" height="103"><polygon points="0,0 384,0 192,86" fill="var(--bronze)"/><circle cx="192" cy="40" r="6" fill="var(--paper)"/></svg>
  </div>
  <div class="envelope" style="top:144px;height:96px">
    <svg width="384" height="96"><polygon points="0,0 384,0 192,80" fill="var(--grey-flap)"/><circle cx="192" cy="36" r="6" fill="var(--paper)"/></svg>
  </div>
  <div class="envelope" style="top:252px;height:108px">
    <svg width="384" height="108"><polygon points="0,0 384,0 192,84" fill="var(--paper-shade)" stroke="#dcdcdc"/><circle cx="192" cy="38" r="6" fill="var(--bronze)"/></svg>
  </div>
  <div class="envelope env-front">
    <div class="wordmark"><span class="dot"></span>Kelumpang</div>
    <p class="line">C27-4, Meranti Square, Jalan Tuaran, 88450 Kota Kinabalu</p>
    <div class="mermaid" role="img" aria-label="Faint mermaid illustration" style="left:270px;top:4px;width:90px;height:60px"></div>
  </div>
  <span class="label" style="left:1080px;top:449px">Envelope Options</span>
</main>
</body>
</html>
```